Swift Heron Parcel & Delivery Services needs a flyer

We need an introductory flyer for a new company based in Yellowknife, Northwest Territories,Canada. Our company name is Swift Heron Parcel & Delivery Services. We will be handling envelopes and small packages up to 20 pounds. We expect 20 percent of our business to come from residential customers and 80 percent from the business community including lawyers, doctors, engineers and government offices. The main message that we will try to convey in this flyer is that we are a new and exciting company that promises to make 100% customer satisfaction our number one goal. I would like the layout to be elegant and simple and certainly not cluttered. It will be a single sided flyer. Text should be easy to read and most likely at most two fonts. I would like one stunning image or photo relating to the courier business and message. There should be plenty of white space throughout the flyer and nice margins on all sides. I would like my flyer to be 8.5 inches by 11 inches and it should read from top to bottom. . I would like a nice big bold headline that in some way mentions " Special Offer- Up to 100% Off. You can change the wording if you have a better idea. Throughout the flyer you can highlight and italicize for emphasis. Please try to use bullet points for my five main reasons for hiring our company which are: you will be 100% satisfied with each delivery or you will be given a complete refund no questions asked, your envelope or package will be delivered on time every time, you will always be treated throughout the delivery process in a professional manner, you will be given the widest selection in Yellowknife of price points and delivery options , you can trust us with your most important and time sensitive deliveries. Try to incorporate something next to these five points to really draw attention like a check mark, star etc.... I would prefer if my company name and contact info is in the bottom third of the flyer. My email is swiftheronparcelyk@mailbox-example.net. My phone number is 867-392-7184. It might be a good idea to have my phone number also at the top of the flyer someplace after the headline saying like Call Now!!! you can use boxes, borders and contrasting bold colors to bring flyer to life. I have a testimonial from a business owner that I dealt with when I ran another business which would be nice to have included . " While receiving daily deliveries for 18 years from Colin Marsh I found him to be punctual , reliable and efficient " Glen Hartley, owner of Hartley and Pruitt Supply LTD, Yellowknife,NWT. I thought perhaps at the top of flyer after the headline perhaps in some way you could say Yellowknife's newest and best courier and delivery service is pleased to offer the following stunning discounts: then you could list the three special offers: 1) First 5 businesses to book regular scheduled deliveries will get 100% off their first delivery. 2) First 5 businesses to book a single delivery will get 50% off that delivery. 3) First 5 residential customers to book a delivery will receive 25% off that delivery. I thought you could mention my name somewhere. Colin Marsh. Owner has lived in Yellowknife for 42 years and has 20 years experience doing performing important and time sensitive deliveries. Perhaps you could mention somewhere that we will have a couple of ongoing discounts also which will be 1) seniors discounts. 2) regular scheduled deliveries discounts. I have suggested colors but if you have other ideas I would certainly look at them. Our business tag line is. On Time Every Time
Target Market(s)
Business owners typically males 30-50 years old
Industry/Entity Type
Delivery Service
Requirements
Must have
- Done in CMYK mode sufficient bleed size for printing
Nice to have
- Nothing set in stone. I recently had my logo design uploaded to this brief. It is up to you if you feel it should be included in the flyer.
Should not have
- I am willing to look at any design

```html
<!DOCTYPE html>
<html lang="en">
<head>
<meta charset="utf-8">
<title>Swift Heron Parcel &amp; Delivery Services – Flyer</title>
<link rel="stylesheet" href="https://fonts.googleapis.com/css2?family=Exo+2:ital,wght@0,400;0,500;0,600;0,700;1,400;1,500;1,600;1,700&display=swap">
<style>
  :root {
    --sky: #3bb3e6;
    --sky-deep: #1f9fd3;
    --teal-a: #1aa6c8;
    --teal-b: #2bc0d8;
    --cream: #fbf6bf;
    --ink: #4a4a4f;
    --grey-text: #5a5a60;
    --footer-bg: #ececf2;
    --white: #ffffff;
    --quote: #3aaee2;
  }
  html, body { margin: 0; padding: 0; overflow: hidden; }
  body { width: 927px; height: 1200px; background: var(--white); font-family: "Exo 2", sans-serif; }
  .flyer { position: relative; width: 927px; height: 1200px; overflow: hidden; background: var(--white); }
  .abs { position: absolute; margin: 0; }

  .header { left: 0; top: 0; width: 927px; height: 258px; background: linear-gradient(90deg, #ffffff 0%, #f6f9fc 60%, #e4eef6 100%); }
  .hero-photo { left: 700px; top: 0; width: 227px; height: 258px; background: linear-gradient(160deg, #e9eef2 0%, #c9a27a 55%, #e6e2dc 100%); }
  .ongoing { left: 30px; top: 30px; font-size: 23px; font-weight: 600; font-style: italic; color: var(--grey-text); white-space: nowrap; }
  .call { left: 500px; top: 70px; color: var(--grey-text); white-space: nowrap; }
  .call small { font-size: 15px; font-weight: 500; margin-right: 4px; }
  .call strong { font-size: 30px; font-weight: 500; }
  .brand { left: 36px; top: 108px; font-size: 58px; line-height: 60px; font-weight: 600; color: var(--sky); }

  .offers { left: 0; top: 258px; width: 927px; height: 315px; background: linear-gradient(120deg, var(--teal-a) 0%, var(--teal-b) 100%); color: var(--white); }
  .offers .intro { position: absolute; left: 42px; top: 14px; font-size: 27px; line-height: 38px; font-weight: 700; font-style: italic; }
  .offer-list, .reasons { list-style: none; padding: 0; margin: 0; position: absolute; }
  .offer-list { left: 82px; top: 108px; font-size: 25px; line-height: 31.5px; font-style: italic; }
  .offer-list li, .reasons li { position: relative; padding-left: 44px; }
  .tick { position: absolute; left: 0; top: 5px; width: 24px; height: 24px; }

  .why { left: 0; top: 573px; width: 927px; height: 495px; background: var(--cream); }
  .scooter-badge { left: 36px; top: 657px; width: 100px; height: 100px; border-radius: 50%; background: var(--white); border: 3px solid #9fd7ef; box-sizing: border-box; }
  .scooter-icon { position: absolute; left: 22px; top: 24px; width: 52px; height: 48px; border-radius: 10px; background: var(--sky); }
  .why-circle { left: 100px; top: 633px; width: 188px; height: 188px; border-radius: 50%; background: var(--sky); color: var(--white); font-size: 38px; font-style: italic; line-height: 42px; display: flex; align-items: center; justify-content: center; text-align: center; }
  .reasons { left: 284px; top: 604px; width: 620px; font-size: 22px; line-height: 32.6px; font-style: italic; color: var(--sky-deep); }
  .reasons .tick { top: 4px; width: 22px; height: 22px; }

  .testimonial { left: 55px; top: 922px; width: 840px; font-size: 26px; line-height: 33px; font-weight: 500; font-style: italic; color: var(--quote); }
  .attribution { right: 36px; top: 990px; text-align: right; color: var(--sky-deep); }
  .attribution .who { font-size: 21px; font-weight: 600; display: block; }
  .attribution .org { font-size: 16px; font-style: italic; display: block; margin-top: 4px; }

  .footer { left: 0; top: 1068px; width: 927px; height: 132px; background: var(--footer-bg); }
  .owner { left: 33px; top: 1086px; width: 480px; font-size: 18.5px; line-height: 31px; color: var(--ink); }
  .owner b { font-weight: 500; }
  .owner i { font-style: italic; }
  .contact { left: 530px; top: 1096px; list-style: none; padding: 0; font-size: 17px; color: var(--ink); }
  .contact li { display: flex; align-items: center; height: 40px; }
  .contact li + li { margin-top: 4px; }
  .contact svg { width: 26px; height: 22px; margin-right: 14px; flex: none; }
</style>
</head>
<body>
<div class="flyer">
  <div class="abs header"></div>
  <div class="abs hero-photo" role="img" aria-label="Photo of a smiling courier in uniform carrying a stack of cardboard parcels"></div>
  <p class="abs ongoing">Seniors discounts &amp; regular scheduled deliveries discounts.</p>
  <p class="abs call"><small>Call now:</small> <strong>867-392-7184</strong></p>
  <h1 class="abs brand">Swift Heron Parcel<br>&amp; Delivery Services</h1>

  <section class="abs offers">
    <p class="intro">Yellowknife’s newest and best courier anddelivery service is<br>pleased to offer the following stunning discounts</p>
    <ul class="offer-list">
      <li><svg class="tick" viewBox="0 0 24 24"><rect x="1.5" y="4.5" width="18" height="18" fill="none" stroke="#fff" stroke-width="2"/><path d="M5 12l5 5L22 3" fill="none" stroke="#f3e98a" stroke-width="3"/></svg>First 5 businesses to book regular scheduled deliveries<br>will get 100% off their first delivery.</li>
      <li><svg class="tick" viewBox="0 0 24 24"><rect x="1.5" y="4.5" width="18" height="18" fill="none" stroke="#fff" stroke-width="2"/><path d="M5 12l5 5L22 3" fill="none" stroke="#f3e98a" stroke-width="3"/></svg>First 5 businesses to book a single delivery<br>will get 50% off that delivery.</li>
      <li><svg class="tick" viewBox="0 0 24 24"><rect x="1.5" y="4.5" width="18" height="18" fill="none" stroke="#fff" stroke-width="2"/><path d="M5 12l5 5L22 3" fill="none" stroke="#f3e98a" stroke-width="3"/></svg>First 5 residential customers to book a delivery<br>will receive 25% off that delivery.</li>
    </ul>
  </section>

  <section class="abs why"></section>
  <div class="abs why-circle"><span>Why<br>us??</span></div>
  <div class="abs scooter-badge"><div class="scooter-icon" role="img" aria-label="Icon of a courier riding a delivery scooter"></div></div>
  <ul class="reasons">
    <li><svg class="tick" viewBox="0 0 24 24"><rect x="1.5" y="4.5" width="18" height="18" fill="none" stroke="#3bb3e6" stroke-width="2"/><path d="M5 12l5 5L22 3" fill="none" stroke="#3bb3e6" stroke-width="3"/></svg>100% satisfaction with each delivery or you will<br>be given acomplete refund noquestions asked,</li>
    <li><svg class="tick" viewBox="0 0 24 24"><rect x="1.5" y="4.5" width="18" height="18" fill="none" stroke="#3bb3e6" stroke-width="2"/><path d="M5 12l5 5L22 3" fill="none" stroke="#3bb3e6" stroke-width="3"/></svg>On time delivery! Every time.</li>
    <li><svg class="tick" viewBox="0 0 24 24"><rect x="1.5" y="4.5" width="18" height="18" fill="none" stroke="#3bb3e6" stroke-width="2"/><path d="M5 12l5 5L22 3" fill="none" stroke="#3bb3e6" stroke-width="3"/></svg>You will always be treated throughout the delivery<br>process in a professional manner,</li>
    <li><svg class="tick" viewBox="0 0 24 24"><rect x="1.5" y="4.5" width="18" height="18" fill="none" stroke="#3bb3e6" stroke-width="2"/><path d="M5 12l5 5L22 3" fill="none" stroke="#3bb3e6" stroke-width="3"/></svg>You will be given the widest selection in Yellowknife<br>of price points and delivery options ,</li>
    <li><svg class="tick" viewBox="0 0 24 24"><rect x="1.5" y="4.5" width="18" height="18" fill="none" stroke="#3bb3e6" stroke-width="2"/><path d="M5 12l5 5L22 3" fill="none" stroke="#3bb3e6" stroke-width="3"/></svg>You can trust us with your most important and<br>time sensitive deliveries.</li>
  </ul>

  <blockquote class="abs testimonial">” While receiving daily deliveries for 18 years from Colin Marsh<br>I found him to be punctual, reliable and efficient ”</blockquote>
  <p class="abs attribution"><span class="who">Glen Hartley</span><span class="org">Hartley and Pruitt Supply LTD, Yellowknife, NWT</span></p>

  <footer class="abs footer"></footer>
  <p class="abs owner"><b>Colin Marsh.</b> <i>Owner has lived in Yellowknife for 42 years and has 20 years experience doing performing important and time sensitive deliveries.</i></p>
  <ul class="abs contact">
    <li><svg viewBox="0 0 26 22"><path d="M2 5l22-3-4 18-7-6-5 5 1-7z" fill="none" stroke="#4a4a4f" stroke-width="1.8" stroke-linejoin="round"/><path d="M9 12L24 2" stroke="#4a4a4f" stroke-width="1.5"/></svg>swiftheronparcelyk@mailbox-example.net</li>
    <li><svg viewBox="0 0 26 22"><path d="M2 8c0-4 22-4 22 0v2h-6V7H8v3H2z" fill="#4a4a4f"/><path d="M6 11h14l3 9H3z" fill="#4a4a4f"/><circle cx="13" cy="15" r="2.6" fill="#ececf2"/></svg>867-392-7184</li>
  </ul>
</div>
</body>
</html>
```